Company Website

We require an online clothing store website for construction workwear.
It needs to be easy to read, user friendly, easy to navigate purchasing.
We are after designs incorporating our recently design logo, and colour combinations black white and orange (same as the company logo). Needs to highlight quality, safety and products. Any ideas around highlighting branding are welcome.

Target Market(s)

Construction workers and businesses.

Industry/Entity Type

Construction

Coding

Coded - Design and coding required

Number of Pages Required

5+ page

Colors
EE7325
F08F49
F5BC92
FAE3D3
FDF4ED

Requirements
Must have
• Include all pictures, prices and details of the products we sell. See PDF uploaded to brief.
Nice to have
• Simple access to purchase items. Easy to navigate website layout.

```html
<!DOCTYPE html>
<html lang="en">
<head>
<meta charset="utf-8">
<title>Guardline Workwear</title>
<link rel="stylesheet" href="https://fonts.googleapis.com/css2?family=Roboto:wght@400;500;700;900&display=swap">
<style>
:root{
  --orange:#ee5a0f;
  --orange-soft:#f08f49;
  --black:#000;
  --ink:#111;
  --white:#fff;
  --grey:#eeeeee;
  --line:#dcdcdc;
  --footer-bar:#1c1c1c;
}
*{box-sizing:border-box;margin:0;padding:0}
html,body{width:1200px;height:3273px;overflow:hidden}
body{font-family:"Roboto",Arial,sans-serif;color:var(--ink);background:var(--white);position:relative}
.abs{position:absolute}
.wordmark{font-weight:900;color:var(--orange);letter-spacing:1px;white-space:nowrap}
.btn{position:absolute;display:flex;align-items:center;justify-content:center;font-weight:700;color:var(--white);text-transform:uppercase;clip-path:polygon(6% 0,100% 0,94% 100%,0 100%)}
.btn-orange{background:var(--orange)}
.btn-black{background:var(--black)}
.btn-white{background:var(--white);color:var(--orange)}
.slash{position:absolute;width:6px;background:var(--white);transform:skewX(-14deg)}

/* header */
.topbar{top:0;left:0;width:1200px;height:105px;background:var(--black)}
.topbar .wordmark{left:95px;top:36px;font-size:28px}
.search{left:408px;top:31px;width:405px;height:40px;border:1px solid #555;color:#bbb;font-size:14px;padding:11px 12px}
.search svg{position:absolute;right:10px;top:11px}
.top-link{color:var(--white);font-size:15px;top:43px}
.mainnav{top:105px;left:0;width:1200px;height:58px;background:var(--orange);border-bottom:3px solid var(--white)}
.mainnav a{position:absolute;top:20px;color:var(--white);font-weight:700;font-size:15px;text-decoration:none}

/* hero */
.hero{top:175px;left:0;width:1200px;height:523px;background:linear-gradient(90deg,#3a3834 0%,#5d5a52 45%,#7a6d5d 70%,#4b4a46 100%)}
.hero .wordmark{left:128px;top:120px;font-size:46px}
.hero h1{position:absolute;left:128px;top:222px;font-size:37px;line-height:43px;font-weight:700;color:var(--white)}
.hero-figure{position:absolute;left:760px;top:30px;width:330px;height:493px;background:linear-gradient(180deg,#d8d5cf 0%,#f07826 35%,#e0621a 70%,#2a2a2a 100%);border-radius:140px 140px 0 0;opacity:.85}

/* categories */
.cat{top:720px;height:363px;display:block}
.cat-photo{position:absolute;inset:0}
.cat h2{position:absolute;width:100%;top:130px;text-align:center;color:var(--white);font-size:34px;font-weight:700}

/* products */
.section-title{top:1192px;width:1200px;text-align:center;font-size:37px;font-weight:700}
.card{top:1274px;width:239px;height:373px;border:1px solid var(--line);border-bottom:4px solid var(--line);background:var(--white)}
.card.active{border-bottom-color:var(--orange)}
.card .photo{position:absolute;left:35px;top:22px;width:168px;height:190px;border-radius:8px}
.card p{position:absolute;top:245px;width:100%;text-align:center;font-size:15px;line-height:18px;color:#333}
.card .btn{top:303px;left:36px;width:150px;height:40px;font-size:15px;text-transform:none}
.arrow{top:1370px}

/* banner */
.banner{top:1778px;left:0;width:1200px;height:444px;background:linear-gradient(90deg,#2c3a48 0%,#5b6a4a 35%,#b8682a 60%,#e06c20 100%)}
.banner h2{position:absolute;left:735px;top:103px;font-size:40px;line-height:46px;font-weight:700;color:var(--white)}

/* about */
.about{top:2282px;left:0;width:1200px;height:421px;background:var(--grey)}
.about h2{position:absolute;left:153px;top:128px;font-size:40px;line-height:46px;font-weight:700}
.about p{position:absolute;left:608px;top:130px;width:455px;font-size:15px;line-height:18px;color:#333;font-family:Arial,sans-serif}

/* features */
.feature{top:2752px}
.feature h3{position:absolute;font-size:18px;font-weight:700;white-space:nowrap}
.feature span{position:absolute;font-size:14px;line-height:17px;color:#444;white-space:nowrap}

/* footer */
.footer{top:2846px;left:0;width:1200px;height:349px;background:var(--black);color:var(--white)}
.footer .wordmark{left:127px;top:68px;font-size:27px}
.footer .blurb{position:absolute;left:127px;top:130px;width:265px;font-size:15px;line-height:18px}
.cards{position:absolute;left:127px;top:245px;display:flex;gap:11px}
.cards div{width:41px;height:27px;border-radius:3px}
.fcol{position:absolute;top:68px}
.fcol h4{color:var(--orange);font-size:17px;font-weight:700;margin-bottom:14px}
.fcol a{display:block;color:var(--white);font-size:15px;text-decoration:none;margin-bottom:12.5px}
.bottombar{top:3195px;left:0;width:1200px;height:78px;background:var(--footer-bar)}
.bottombar .copy{position:absolute;left:123px;top:30px;color:var(--white);font-size:15px}
.join{position:absolute;left:828px;top:0;width:268px;height:78px;background:var(--orange);clip-path:polygon(8% 0,100% 0,92% 100%,0 100%)}
.join b{position:absolute;left:35px;top:34px;color:var(--white);font-size:17px}
.social{position:absolute;top:28px;width:26px;height:26px;border-radius:50%;background:var(--orange-soft)}
</style>
</head>
<body>

<header class="abs topbar">
  <div class="abs wordmark">GUARDLINE WORKWEAR</div>
  <div class="abs search">Search Products
    <svg width="16" height="16" viewBox="0 0 16 16"><circle cx="6.5" cy="6.5" r="5" fill="none" stroke="#fff" stroke-width="2"/><path d="M10 10l4.5 4.5" stroke="#fff" stroke-width="2"/></svg>
  </div>
  <svg class="abs" style="left:850px;top:42px" width="18" height="18" viewBox="0 0 18 18"><circle cx="9" cy="5" r="4" fill="none" stroke="#fff" stroke-width="1.6"/><path d="M1 17c1-5 15-5 16 0" fill="none" stroke="#fff" stroke-width="1.6"/></svg>
  <span class="abs top-link" style="left:879px">Login</span>
  <svg class="abs" style="left:942px;top:42px" width="22" height="19" viewBox="0 0 22 19"><path d="M11 18L2.5 9.5A5 5 0 0 1 11 3a5 5 0 0 1 8.5 6.5z" fill="none" stroke="#ee5a0f" stroke-width="2"/></svg>
  <svg class="abs" style="left:988px;top:38px" width="22" height="24" viewBox="0 0 22 24"><path d="M2 8h18l-1 15H3z" fill="#fff"/><path d="M7 8V5a4 4 0 0 1 8 0v3" fill="none" stroke="#fff" stroke-width="2"/></svg>
  <div class="abs" style="left:1005px;top:35px;width:16px;height:16px;border-radius:50%;background:var(--orange);color:#fff;font-size:11px;text-align:center;line-height:16px;font-weight:700">0</div>
  <span class="abs top-link" style="left:1023px">Cart(0)</span>
</header>

<nav class="abs mainnav">
  <a style="left:125px">HOME</a><a style="left:226px">MEN'S</a><a style="left:329px">WOMEN'S</a><a style="left:456px">FLX &amp; MOVE</a><a style="left:602px">FLAME RESISTANT</a><a style="left:797px">SHOP BY RANGE</a><a style="left:980px">WORK WEAR</a>
</nav>

<section class="abs hero" role="img" aria-label="Photo of a smiling woman in a white hard hat and orange hi-vis jacket at a construction site">
  <div class="hero-figure"></div>
  <div class="abs wordmark">GUARDLINE WORKWEAR</div>
  <h1>LOREM IPSUM DOLOR SIT<br>AMETCONSECTETUR</h1>
  <a class="btn btn-orange" style="left:128px;top:338px;width:185px;height:53px;font-size:18px">Shop Now</a>
  <div class="slash" style="left:313px;top:338px;height:53px"></div>
</section>

<section class="abs cat" style="left:0;width:587px">
  <div class="cat-photo" role="img" aria-label="Photo of a construction worker in a hard hat and yellow hi-vis shirt" style="background:linear-gradient(120deg,#4a4030 0%,#8a7a40 45%,#b8b832 70%,#3a3a30 100%)"></div>
  <h2>CONSTRUCTION SHIRTS</h2>
  <a class="btn btn-orange" style="left:136px;top:185px;width:130px;height:37px;font-size:15px">Shop Men's</a>
  <a class="btn btn-white" style="left:262px;top:185px;width:160px;height:37px;font-size:15px">Shop Women's</a>
</section>
<section class="abs cat" style="left:608px;width:592px">
  <div class="cat-photo" role="img" aria-label="Photo of a worker in yellow and black work pants beside a ladder" style="background:linear-gradient(120deg,#3a3a36 0%,#6a6040 40%,#a8902c 70%,#2a2a28 100%)"></div>
  <h2>CONSTRUCTION PANTS</h2>
  <a class="btn btn-orange" style="left:146px;top:185px;width:130px;height:37px;font-size:15px">Shop Men's</a>
  <a class="btn btn-white" style="left:272px;top:185px;width:160px;height:37px;font-size:15px">Shop Women's</a>
</section>

<h2 class="abs section-title">LATEST PRODUCTS</h2>
<svg class="abs arrow" style="left:24px" width="22" height="34" viewBox="0 0 22 34"><path d="M18 3L4 17l14 14" fill="none" stroke="#111" stroke-width="4"/></svg>
<svg class="abs arrow" style="left:1141px" width="22" height="34" viewBox="0 0 22 34"><path d="M4 3l14 14L4 31" fill="none" stroke="#111" stroke-width="4"/></svg>

<article class="abs card active" style="left:86px">
  <div class="photo" role="img" aria-label="Orange and navy two-toned long sleeve shirt with reflective tape" style="background:linear-gradient(180deg,#f07826 0%,#f07826 50%,#1e2440 100%)"></div>
  <p>MENS L/S TWO-TONED<br>VENTED TAPED SHIRT</p>
  <a class="btn btn-orange">View Product</a>
</article>
<article class="abs card" style="left:349px">
  <div class="photo" role="img" aria-label="Orange long sleeve vented shirt with reflective tape" style="background:linear-gradient(180deg,#f4832e,#e8621a)"></div>
  <p>MENS L/S STANDARD<br>VENTED ORANGE SHIRT</p>
  <a class="btn btn-black">View Product</a>
</article>
<article class="abs card" style="left:612px">
  <div class="photo" role="img" aria-label="Yellow and orange hi-vis long sleeve polos with navy lower half" style="background:linear-gradient(135deg,#d8f040 0%,#c8e040 40%,#f07826 60%,#1e2440 100%)"></div>
  <p>HI- VIS L/S POLO</p>
  <a class="btn btn-black">View Product</a>
</article>
<article class="abs card" style="left:875px">
  <div class="photo" role="img" aria-label="Navy work pants with reflective bands" style="background:linear-gradient(180deg,#2a3260,#1a1f40)"></div>
  <p>HI-VIS NAVY PANTS</p>
  <a class="btn btn-black">View Product</a>
</article>

<section class="abs banner" role="img" aria-label="Photo of two engineers in hard hats and hi-vis jackets looking at a laptop">
  <h2>A PERFECT CHOICE<br>FOR THE WORKING<br>TRADESMEN</h2>
  <a class="btn btn-black" style="left:735px;top:259px;width:185px;height:53px;font-size:18px">Shop Now</a>
  <div class="slash" style="left:922px;top:259px;height:53px"></div>
</section>

<section class="abs about">
  <h2>ABOUT GUARDLINE<br>WORKWEAR</h2>
  <a class="btn btn-orange" style="left:153px;top:243px;width:190px;height:53px;font-size:18px">Read More</a>
  <div class="slash" style="left:340px;top:243px;height:53px;background:#000"></div>
  <p>Lorem ipsum dolor sit amet, consectetur adipiscing elit, sed do eiusmod tempor incididunt ut labore et dolore magna aliqua. Qui s ipsum suspendisse ultrices gravida. Risus commodo viverra maecenas accumsan lacus vel facilisis. Lorem ipsum dolor sit am et, consectetur adipiscing elit, sed do eiusmod tempor incididunt ut labore et dolore magna aliqua. Quis ipsum suspendisse ultrices gravida. Risus commodo viverra maecenas accumsan lacus vel facilmmodo viverra maeisis.</p>
</section>

<div class="abs feature" style="left:122px">
  <svg class="abs" style="left:0;top:0" width="60" height="44" viewBox="0 0 60 44"><path d="M2 4h34v28H2zM36 14h12l9 10v8H36z" fill="none" stroke="#111" stroke-width="2.5"/><circle cx="14" cy="35" r="5" fill="#fff" stroke="#111" stroke-width="2.5"/><circle cx="46" cy="35" r="5" fill="#fff" stroke="#111" stroke-width="2.5"/><path d="M8 14h16" stroke="#ee5a0f" stroke-width="3"/></svg>
  <h3 style="left:73px;top:-2px">FREE SHIPPING</h3>
  <span style="left:74px;top:24px">Lorem ipsum dolor sit ametcon<br>se ctetur adipiscing elit.</span>
</div>
<div class="abs feature" style="left:485px">
  <svg class="abs" style="left:0;top:-2px" width="54" height="54" viewBox="0 0 54 54"><path d="M8 20A21 21 0 1 1 10 40" fill="none" stroke="#111" stroke-width="2.5"/><path d="M4 14l4 7 7-4" fill="none" stroke="#111" stroke-width="2.5"/><path d="M18 22l9-5 9 5v11l-9 5-9-5z" fill="#ee5a0f"/></svg>
  <h3 style="left:70px;top:-2px">FREE RETURNS</h3>
  <span style="left:71px;top:24px">Lorem ipsum dolor sit ametcon<br>se ctetur adipiscing elit.</span>
</div>
<div class="abs feature" style="left:805px">
  <svg class="abs" style="left:0;top:0" width="48" height="48" viewBox="0 0 48 48"><path d="M6 4l8-1 5 10-5 4c3 7 8 12 15 15l4-5 10 5-1 8c-20 2-38-16-36-36z" fill="none" stroke="#111" stroke-width="2.5"/><rect x="24" y="8" width="20" height="14" fill="none" stroke="#ee5a0f" stroke-width="2.5"/><path d="M24 8l10 8 10-8" fill="none" stroke="#ee5a0f" stroke-width="2.5"/></svg>
  <h3 style="left:62px;top:-2px">CONTACT US</h3>
  <span style="left:63px;top:24px">Lorem ipsum dolor sit ametcon<br>+1 555-010-2040</span>
</div>

<footer class="abs footer">
  <div class="abs wordmark">GUARDLINE WORKWEAR</div>
  <p class="blurb">Lorem ipsum dolor sit amet, conse ctetur adipiscing elit, sed do eiusmod tempor incididunt ut labore et dolore magna aliqua.</p>
  <div class="cards" aria-label="Accepted payment cards">
    <div style="background:#1a3a8a"></div><div style="background:#2a3a6a"></div><div style="background:#2f6fc0"></div><div style="background:#3070c0"></div><div style="background:#333"></div>
  </div>
  <div class="fcol" style="left:481px"><h4>HELP</h4><a>Store Locator</a><a>Click &amp; Collect</a><a>Delivery &amp; Returns</a><a>Sizing Charts</a><a>Fitting Guide</a><a>Contact Us</a><a>FAQs</a></div>
  <div class="fcol" style="left:690px"><h4>RESOURCES</h4><a>Tender Inquiries</a><a>Safety Resource Centre</a><a>Safety Catalogues</a><a>Discount Program</a><a>Check Gift Card</a><a>FAQs</a></div>
  <div class="fcol" style="left:922px"><h4>ABOUT</h4><a>About Us</a><a>Sitemap</a><a>Search</a><a>Rewards</a><a>Privacy Policy</a><a>Terms and Conditions</a></div>
</footer>

<div class="abs bottombar">
  <p class="copy">© Copyright 2024 All rights reserved.</p>
  <div class="join">
    <b>JOIN NOW</b>
    <span class="social" style="left:138px"></span>
    <span class="social" style="left:167px"></span>
    <span class="social" style="left:196px"></span>
  </div>
</div>

</body>
</html>
```